依頼詳細
主な参加者は女性になりますので、女性的なデザインでお願いします。バナー制作ですが、ポスターのように縦長サイズのイメージになります。
記載項目
バナーに記載していただきたい内容は以下のとおりです。

---ここから---

2月4日は『妊娠の日』
業界初!マタニティヨガインストラクターと鍼灸師がコラボ!
妊活体操イベント開催

<妊活体操イベント概要>
開催日時:2017年2月4日(土)13:00~14:00
*館内着に着替えるため、余裕をもって30分以上前のご来場をお願いいたします。
開催場所:SPA ORIN(神奈川県横浜市西区南空3-5-7 ソラモールクレオ内)

◆当日のプログラム内容
⑴ご挨拶・趣旨説明
⑵マタニティヨガの話・葉酸の話・にんかツボの話
⑶妊活体操
⑷質疑応答

参加費:3,000円(入館料2,880円を含む)
定員:30名(カップルでのご来場もお待ちしております。)
備考:イベント終了後はSPA ORIN内の施設をご利用いただけます。
(深夜3時以降は別途1,730円の利用料が必要です。)

---ここまで---

妊活体操をイメージできるような画像の使用をお願いいたします。
(後日、こちらで撮影した写真に差し替えを行います。)

なお、イベントの会場はこちらになります。
http://www.spa-orin-web.jp/

イベントの告知・集客はこちらのサイトで行います。
http://mirefolle.com/
サイズ
• 横768px(縦は自由です)
希望イメージ
シンプル 複雑
単色 カラフル
暗い 明るい
日常 高級
遊び心 厳粛
未来的 伝統的
女性的 男性的
希望する色
赤系、茶系、妊活ですのでピンク系を使っていただくようお願いいたします。
納品ファイル
• 高解像度JPG (.jpg)
補足説明
◆コンペ参加条件
・1/16に本イベントに関する撮影を行いますので、イメージ写真の差し替え対応までできる方(今回のコンペ費用に含みます。)
・今後定期的にイベントを開催する方向で検討しておりますので、その際は開催日時や開催場所の修正対応をお願いできる方(こちらは別途2,000円/回の費用をお支払いします。手数料込、税別)
弊社スケジュールの都合により、締切を1/5に変更させていただきます。
ご提案どうぞよろしくお願いいたします。

必要な情報が一番目立つようにレイアウトされており、その他の情報もスッキリと分かりやすく書かれていることで、パソコンでみてもスマホでみても視認性が高かった点を評価させていただきました。女性的な雰囲気もイメージどおりでした。

今回は多数の素敵な提案をいただき感謝しております。どうもありがとうございました。

```html
<!DOCTYPE html>
<html lang="ja">
<head>
<meta charset="utf-8">
<title>妊活体操イベント開催</title>
<link href="https://fonts.googleapis.com/css2?family=M+PLUS+Rounded+1c:wght@500;700;800;900&family=Kosugi+Maru&display=swap" rel="stylesheet">
<style>
  :root{
    --pink:#e8538a;
    --pink-deep:#e03f7b;
    --pink-soft:#fbe0ea;
    --pink-pale:#fff3f7;
    --orange:#f0883a;
    --orange-soft:#fbd9b8;
    --green-pale:#f4f8e4;
    --text:#4a3a3a;
    --white:#ffffff;
  }
  html,body{margin:0;padding:0;overflow:hidden;}
  body{width:681px;height:1200px;background:var(--white);font-family:"Kosugi Maru","M PLUS Rounded 1c",sans-serif;color:var(--text);}
  .banner{position:relative;width:681px;height:1200px;overflow:hidden;background:var(--pink-pale);}
  .hero{position:absolute;left:0;top:0;width:681px;height:520px;background:var(--pink-soft);}
  .hero-illustration{position:absolute;left:318px;top:0;width:363px;height:520px;
    background:radial-gradient(ellipse at 55% 45%,#f7c7a8 0%,#f4a9c0 45%,#fbe0ea 80%);}
  .outline{text-shadow:-3px -3px 0 var(--white),3px -3px 0 var(--white),-3px 3px 0 var(--white),3px 3px 0 var(--white),0 3px 0 var(--white),0 -3px 0 var(--white),3px 0 0 var(--white),-3px 0 0 var(--white);}
  .date-badge{position:absolute;left:16px;top:16px;width:96px;height:70px;border-radius:14px;background:var(--pink);color:var(--white);
    font:900 46px/70px "M PLUS Rounded 1c",sans-serif;text-align:center;}
  .date-title{position:absolute;left:122px;top:30px;font:800 38px/1 "M PLUS Rounded 1c",sans-serif;color:var(--pink-deep);}
  .ruby-num{position:absolute;top:-20px;font-size:16px;}
  .lead{position:absolute;left:24px;top:102px;font:900 31px/1 "M PLUS Rounded 1c",sans-serif;color:var(--pink-deep);}
  .role{position:absolute;left:40px;font:900 44px/1.2 "M PLUS Rounded 1c",sans-serif;color:var(--pink);}
  .role-yoga{top:156px;}
  .cross{position:absolute;left:140px;top:262px;font:900 60px/1 "M PLUS Rounded 1c",sans-serif;color:var(--pink-deep);}
  .role-acu{top:340px;left:80px;font-size:56px;}
  .role-acu .furi{position:absolute;top:-16px;left:0;width:100%;text-align:center;font-size:15px;letter-spacing:10px;}
  .main-title{position:absolute;left:24px;top:410px;font:900 84px/1 "M PLUS Rounded 1c",sans-serif;color:var(--orange);letter-spacing:2px;}
  .main-title .pk{color:var(--pink);}
  .main-sub{position:absolute;left:420px;top:450px;font:800 32px/1 "M PLUS Rounded 1c",sans-serif;color:var(--pink-deep);}
  .overview-band{position:absolute;left:30px;top:524px;width:621px;height:38px;border-radius:19px;background:var(--pink);color:var(--white);
    font:800 26px/38px "M PLUS Rounded 1c",sans-serif;text-align:center;}
  .info-row{position:absolute;left:30px;display:flex;align-items:center;gap:14px;}
  .label{background:var(--pink);color:var(--white);font:800 22px/1 "M PLUS Rounded 1c",sans-serif;padding:7px 10px;border-radius:4px;}
  .info-main{font:800 27px/1 "M PLUS Rounded 1c",sans-serif;color:var(--text);}
  .note{position:absolute;left:44px;font-size:15px;color:var(--text);}
  .venue{position:absolute;left:180px;top:706px;font:900 30px/1 "M PLUS Rounded 1c",sans-serif;}
  .address{position:absolute;left:180px;top:742px;font-size:18px;}
  .program{position:absolute;left:14px;top:790px;width:330px;height:395px;background:var(--green-pale);border:2px solid var(--orange-soft);border-radius:10px;overflow:hidden;}
  .program-head{background:var(--orange);color:var(--white);font:800 26px/44px "M PLUS Rounded 1c",sans-serif;text-align:center;}
  .program-list{list-style:none;margin:0;padding:6px 16px;}
  .program-list li{font:700 22px/1.35 "M PLUS Rounded 1c",sans-serif;padding:14px 0;border-bottom:2px dotted var(--orange);}
  .program-list li:last-child{border-bottom:none;}
  .fees{position:absolute;left:356px;top:792px;width:310px;}
  .fee-row{display:flex;align-items:center;gap:12px;margin-bottom:22px;}
  .circle{width:66px;height:66px;border-radius:50%;background:var(--pink);color:var(--white);font:800 17px/1.1 "M PLUS Rounded 1c",sans-serif;
    display:flex;align-items:center;justify-content:center;text-align:center;flex:none;}
  .fee-value{font:900 34px/1 "M PLUS Rounded 1c",sans-serif;}
  .fee-small{font-size:14px;margin-top:6px;}
  .remark{border:2px solid var(--pink);border-radius:8px;background:var(--white);padding:10px 12px;font-size:15px;line-height:1.5;}
  .remark small{display:block;font-size:12px;}
</style>
</head>
<body>
<main class="banner">
  <section class="hero">
    <div class="hero-illustration" role="img" aria-label="お腹に手を当てる妊婦の女性のイラスト"></div>
    <div class="date-badge">2/4</div>
    <div class="date-title">は『<span style="position:relative">妊<span class="ruby-num" style="left:10px">2</span></span><span style="position:relative">娠<span class="ruby-num" style="left:10px">4</span></span>の日』</div>
    <div class="lead outline">業界初のコラボレーション!</div>
    <div class="role role-yoga outline">マタニティヨガ<br>インストラクター</div>
    <div class="cross outline">×</div>
    <div class="role role-acu outline"><span class="furi">しんきゅうし</span>鍼灸師</div>
    <div class="main-title outline"><span class="pk">妊活</span>体操</div>
    <div class="main-sub outline">イベント開催</div>
  </section>

  <div class="overview-band">〜 妊活体操イベント概要 〜</div>

  <div class="info-row" style="top:580px"><span class="label">開催日時</span><span class="info-main">2017年2月4日(土)13:00〜14:00</span></div>
  <p class="note" style="top:610px;margin:0">*館内着に着替えるため、余裕をもって30分以上前のご来場をお願いいたします。</p>

  <div class="info-row" style="top:660px"><span class="label">開催場所</span></div>
  <div class="venue">SPA ORIN</div>
  <div class="address">神奈川県横浜市西区南空3-5-7 ソラモールクレオ内</div>

  <section class="program">
    <div class="program-head">当日のプログラム</div>
    <ol class="program-list">
      <li>ご挨拶・趣旨説明</li>
      <li>マタニティヨガの話・葉酸の話・にんかツボの話</li>
      <li>妊活体操</li>
      <li>質疑応答</li>
    </ol>
  </section>

  <section class="fees">
    <div class="fee-row"><span class="circle">参加費</span>
      <div><div class="fee-value">3,000円</div><div class="fee-small">(入館料2,880円を含む)</div></div></div>
    <div class="fee-row"><span class="circle">定員</span>
      <div><div class="fee-value">30名</div><div class="fee-small">カップルでのご来場も<br>お待ちしております。</div></div></div>
    <div class="remark">イベント終了後はSPA ORIN内の施設をご利用いただけます。<small>(深夜3時以降は別途1,730円の利用料が必要です。)</small></div>
  </section>
</main>
</body>
</html>
```